Design a Flash-card (Two-sided Study Card)

I need a talented graphics designer to make a flashcard (study-card) template in .psd format, which I'll able to edit (front side + back side).

See rough design idea attached - but feel free to make it look nice according to your artistic sense. It needs to be simple yet impressive - something people would look at and want to have.

The main requirement is that it's a 2-side flashcard, meaning one word on one side and one on the other. There should be enough space to write up to 10 translations on one of the sides, because words can have different meanings; also the design should include space for 1-2 sentence examples.

See rough design attached,

Looking forward to your submissions,

Thank you.

```html
<!DOCTYPE html>
<html lang="en">
<head>
<meta charset="utf-8">
<title>Flashcard Template – Front and Back</title>
<link rel="stylesheet" href="https://fonts.googleapis.com/css2?family=Montserrat:wght@600;700&family=Raleway:wght@400;500&display=swap">
<style>
  :root {
    --stage: #5f5f5f;
    --card: #f0f0f0;
    --accent: #1a87a8;
    --rule: #333333;
    --heading: #2b2b2b;
    --body: #2d4a6b;
    --bullet: #173a63;
    --photo-top: #c9b9a3;
    --photo-bottom: #8c7a68;
  }
  * { margin: 0; padding: 0; box-sizing: border-box; }
  html, body { width: 1200px; height: 1176px; overflow: hidden; }
  body { background: var(--stage); position: relative; font-family: "Raleway", sans-serif; }

  .card {
    position: absolute; left: 199px; width: 783px;
    background: var(--card);
  }
  .card--front { top: 55px; height: 447px; }
  .card--back { top: 605px; height: 446px; }

  .band { position: absolute; background: var(--accent); }
  .rule { position: absolute; left: 0; width: 100%; background: var(--rule); }

  .heading {
    position: absolute; font-family: "Montserrat", sans-serif; font-weight: 700;
    color: var(--heading); font-size: 26px; line-height: 1;
  }

  /* Front */
  .front-band-left { left: 0; top: 149px; width: 309px; height: 26px; }
  .front-band-right { left: 473px; top: 149px; width: 310px; height: 26px; }
  .word-title { left: 0; width: 783px; top: 150px; text-align: center; }
  .definition {
    position: absolute; left: 0; width: 783px; top: 213px; text-align: center;
    color: var(--body); font-size: 22px; line-height: 28px;
  }
  .front-rule { top: 405px; height: 7px; }
  .front-bottom-band { left: 0; top: 421px; width: 100%; height: 26px; }

  /* Back */
  .photo {
    position: absolute; left: 31px; top: 21px; width: 188px; height: 210px;
    border: 5px solid var(--rule);
    background: linear-gradient(160deg, var(--photo-top), var(--photo-bottom));
  }
  .photo-band-left { left: 0; top: 45px; width: 31px; height: 24px; }
  .photo-band-right { left: 219px; top: 45px; width: 36px; height: 24px; }
  .translation-title { left: 264px; top: 46px; }

  .translations {
    position: absolute; left: 372px; top: 82px; list-style: none;
    display: grid; grid-template-columns: 200px 200px; row-gap: 13px;
    color: var(--body); font-size: 21px; line-height: 30px;
    grid-auto-flow: row;
  }
  .translations li { display: flex; align-items: center; gap: 3px; }
  .translations li::before {
    content: ""; width: 13px; height: 13px; border-radius: 50%;
    background: var(--bullet); flex: none;
  }

  .examples-band { left: 0; top: 297px; width: 431px; height: 26px; }
  .examples-title { left: 445px; top: 298px; }
  .examples {
    position: absolute; left: 75px; width: 650px; top: 335px;
    color: var(--body); font-size: 21.5px; line-height: 28px;
  }
  .back-rule { top: 411px; height: 6px; }
  .back-bottom-band { left: 0; top: 421px; width: 100%; height: 25px; }
</style>
</head>
<body>
  <section class="card card--front" aria-label="Flashcard front">
    <div class="band front-band-left"></div>
    <div class="band front-band-right"></div>
    <h1 class="heading word-title">WORD</h1>
    <p class="definition">WORD WORD WORD WORD WORD WORD WORD WORD<br>WORD WORD WORD WORD WORD WORD WORD WORD</p>
    <div class="rule front-rule"></div>
    <div class="band front-bottom-band"></div>
  </section>

  <section class="card card--back" aria-label="Flashcard back">
    <div class="band photo-band-left"></div>
    <div class="band photo-band-right"></div>
    <div class="photo" role="img" aria-label="Portrait photo of the learner"></div>
    <h2 class="heading translation-title">Translation</h2>
    <ul class="translations">
      <li>Translation</li><li>Translation</li>
      <li>Translation</li><li>Translation</li>
      <li>Translation</li><li>Translation</li>
      <li>Translation</li><li>Translation</li>
      <li>Translation</li><li>Translation</li>
    </ul>
    <div class="band examples-band"></div>
    <h2 class="heading examples-title">Sentence Examples</h2>
    <p class="examples">Sentence Example Sentence Example Sentence Sentence<br>Example Sentence Example Sentence Sentence Sentence</p>
    <div class="rule back-rule"></div>
    <div class="band back-bottom-band"></div>
  </section>
</body>
</html>
```